Pellworth and Tasker Ranch Insurance

Would like you all to design a logo for our Business cards and possible letterhead.
This business provides Ranch insurance for folks in Texas, New Mexico, and Oklahoma

Ggood stuff everybody, be sure to include email and Mobil for both of us on all designs

Thanks

Hello All

Wanted to let you all know i am going to extend deadline a few days, and add some more $$ to the budget

Reason: Give everybody a bit ,more time, and I added more money

Appreciate all of yalls hard work, will review and provide feed back hopefully today, been a little whacky with the holidays and all

Industry/Entity Type

Business

```html
<!DOCTYPE html>
<html lang="en">
<head>
<meta charset="utf-8">
<title>Pellworth and Tasker – Business Card</title>
<link href="https://fonts.googleapis.com/css2?family=Arimo:wght@400&display=swap" rel="stylesheet">
<style>
  :root {
    --saddle: #7d4e39;
    --amber: #ef9235;
    --rust: #b5612a;
    --rule: #c4692b;
    --ink-light: #ffffff;
    --ink-dark: #7d4e39;
    --edge: #8a8a8a;
  }
  html, body {
    margin: 0;
    padding: 0;
    width: 1200px;
    height: 726px;
    overflow: hidden;
    background: #ffffff;
  }
  .card {
    position: relative;
    width: 1198px;
    height: 724px;
    border: 1px solid var(--edge);
    border-radius: 50px;
    overflow: hidden;
    background: var(--amber);
    font-family: "Arimo", Arial, sans-serif;
  }
  .card__panel {
    position: absolute;
    left: 0; top: 0;
    width: 422px;
    height: 100%;
    background: var(--saddle);
  }
  .brand {
    position: absolute;
    left: 372px;
    top: 76px;
    display: flex;
    align-items: center;
    gap: 14px;
  }
  .brand__mark {
    width: 70px;
    height: 70px;
    border-radius: 50%;
    background: var(--ink-light);
  }
  .brand__name {
    color: var(--ink-light);
    font-size: 38px;
    line-height: 1;
    margin-top: 44px;
  }
  .contact {
    position: absolute;
    top: 262px;
    text-align: center;
    line-height: 1;
  }
  .contact--left { left: 0; width: 422px; color: var(--ink-light); }
  .contact--right { left: 760px; width: 440px; color: var(--ink-dark); }
  .contact__name { font-size: 45px; margin: 0 0 22px; font-weight: 400; }
  .contact__line { font-size: 29px; margin: 0 0 16px; }
  .divider {
    position: absolute;
    left: 422px; right: 0;
    top: 492px;
    height: 7px;
    background: var(--rule);
  }
  .info-bar {
    position: absolute;
    left: 422px;
    background: var(--rust);
    color: var(--ink-dark);
    font-size: 34px;
    line-height: 1;
    padding-left: 29px;
    box-sizing: border-box;
    display: flex;
    align-items: center;
  }
  .info-bar--address { top: 511px; height: 52px; right: 0; }
  .info-bar--phone { top: 573px; height: 49px; width: 426px; }
  .info-bar--web { top: 633px; height: 50px; width: 519px; }
</style>
</head>
<body>
  <div class="card">
    <div class="card__panel"></div>

    <div class="brand">
      <div class="brand__mark"></div>
      <div class="brand__name">Pellworth and Tasker</div>
    </div>

    <div class="contact contact--left">
      <h2 class="contact__name">Wade Pellworth</h2>
      <p class="contact__line">512-555-0147</p>
      <p class="contact__line">pellworthw@ranchco.com</p>
    </div>

    <div class="contact contact--right">
      <h2 class="contact__name">T.Ray Tasker</h2>
      <p class="contact__line">325-555-0186</p>
      <p class="contact__line">ray@pellworthandtasker.com</p>
    </div>

    <div class="divider"></div>
    <div class="info-bar info-bar--address">Address : 418 W Oak St. Mesa Verde, TX 76999</div>
    <div class="info-bar info-bar--phone">Phone : 325-555-0123</div>
    <div class="info-bar info-bar--web">www.pellworthandtasker.com</div>
  </div>
</body>
</html>
```